Junk Removal company with existing WordPress website needs new mobile enhanced website

I am looking to have someone take my existing website and either update it with a new design and menu which is more mobile enhanced (70% of my traffic is from mobile devices and most people stay on the home page to find what they need) or create a new website from scratch to achieve my design goals. My name goal is the have to home page be quick and easy to find what the customer is looking for.
Our current website is: BrightCreekJunkOut.com and Google my business page https://g.page/brightcreekjunkout
I have attached an example the design idea I came up with for the home page based on what I would like it to look like as well as some logo files and pictures.

```html
<!DOCTYPE html>
<html lang="en">
<head>
<meta charset="utf-8">
<title>Bright Creek Junk Out – Mobile Home</title>
<link rel="stylesheet" href="https://fonts.googleapis.com/css2?family=Outfit:wght@300;400;500;600;700;800&display=swap">
<style>
:root{
  --orange:#ff9900;
  --ink:#1c1c1c;
  --text:#444;
  --muted:#777;
  --black:#151515;
  --soft:#f6f6fb;
  --line:#d8d8de;
  --sky-top:#6f8fd3;
  --sky-bottom:#9fb6e6;
  --night:#17222e;
  --night-deep:#0e151d;
  --page:#e7e7e7;
}
*{margin:0;padding:0;box-sizing:border-box}
html,body{width:1200px;height:3346px;overflow:hidden;background:var(--page)}
body{font-family:"Outfit",sans-serif;color:var(--text);position:relative}
.screen{position:absolute;left:401px;top:90px;width:470px;height:3195px;background:#fff;overflow:hidden}
.abs{position:absolute}
.center{left:0;width:100%;text-align:center}

/* header */
.site-header{left:0;top:0;width:470px;height:67px;background:var(--black);z-index:3}
.menu-toggle{left:24px;top:24px;width:24px}
.menu-toggle span{display:block;height:2px;background:#fff;margin-bottom:5px}
.brand{left:155px;top:14px;width:160px;height:40px;display:flex;align-items:center;justify-content:center;gap:6px;color:#fff;font-weight:700;font-size:15px;letter-spacing:.5px}
.brand i{width:10px;height:10px;background:var(--orange);display:block}
.btn-estimate{left:344px;top:17px;width:107px;height:31px;background:var(--orange);color:#fff;font-size:12px;font-weight:600;display:flex;align-items:center;justify-content:center}

/* hero */
.hero{left:0;top:67px;width:470px;height:435px;background:linear-gradient(180deg,var(--sky-top),var(--sky-bottom));overflow:hidden;border-bottom-left-radius:50% 34px;border-bottom-right-radius:50% 34px}
.hero-title{top:90px;color:#fff;font-size:31px;font-weight:300;letter-spacing:-.3px}
.hero-title b{font-weight:800}
.hero-sub{top:128px;color:#fff;font-size:12.5px}
.btn-call{left:145px;top:191px;width:180px;height:30px;background:var(--orange);color:#fff;font-size:9px;font-weight:600;display:flex;align-items:center;justify-content:center;gap:8px}
.hero-photo{left:0;top:240px;width:470px;height:195px;background:linear-gradient(180deg,#7d9a76 0%,#5f6a58 45%,#2d2f30 100%)}
.hero-edge{left:0;top:495px;width:470px;height:10px}

/* intro */
.rule{height:2px;width:30px;background:var(--orange)}
.h2{color:var(--ink);font-weight:500}
.intro-title{top:556px;font-size:22px}
.intro-text{top:588px;font-size:13px;line-height:20px;color:#333}
.intro-circle{left:225px;top:650px;width:200px;height:250px;border-radius:50%;background:var(--soft)}
.hex-photo{left:135px;top:674px}
.badge{left:73px;top:802px;width:82px;height:30px;background:var(--orange);color:#fff;display:flex;align-items:center;gap:5px;padding-left:7px;font-size:12px}
.badge small{font-size:7px;line-height:8px}
.intro-body{top:934px;left:48px;width:374px;font-size:12px;line-height:24px;text-align:center;color:#444}
.btn-outline{left:157px;top:1049px;width:153px;height:36px;border:1.5px solid var(--orange);border-radius:18px;color:var(--ink);font-size:13px;font-weight:500;display:flex;align-items:center;justify-content:center}

/* services */
.services{left:0;top:1132px;width:470px;height:790px;background:var(--soft)}
.services-title{top:135px;font-size:30px}
.services-sub{top:175px;font-size:12px;color:#444}
.slide-arrow{top:377px;width:27px;height:58px;background:#4a4a4a;display:flex;align-items:center;justify-content:center}
.slide-arrow.prev{left:0;background:#e2e2e8}
.slide-arrow.next{left:443px}
.service-name{top:555px;font-size:28px}
.dotted{left:64px;top:611px;width:312px;border-top:2px dotted #bbb}
.service-list{top:636px;width:470px;font-size:15px;color:#444;line-height:28.5px}
.service-list ul{list-style:none;position:absolute;top:0}
.dots{display:flex;gap:5px;justify-content:center;align-items:center}
.dots i{width:6px;height:6px;border-radius:50%;background:#aaa;display:block}
.dots i.on{width:9px;height:9px;background:var(--orange)}

/* testimonial */
.quote-card{left:48px;top:1974px;width:367px;height:185px;border:1px solid #f0f0f0;box-shadow:0 0 8px rgba(0,0,0,.04)}
.quote-mark{left:25px;top:18px;color:var(--orange);font-size:38px;font-weight:700;line-height:1}
.quote-text{left:64px;top:28px;width:280px;font-size:11px;line-height:21px;color:#555}
.avatar{left:74px;top:2191px;width:32px;height:32px;border-radius:50%;background:#3b4a66;border:2px solid #8bc34a}
.author{left:128px;top:2191px;font-size:10.5px;font-weight:600;color:var(--ink);letter-spacing:.4px}
.author small{display:block;font-weight:400;color:#888;font-size:9px;letter-spacing:0;margin-top:6px}
.ring-dots{top:2252px;display:flex;gap:5px;justify-content:center}
.ring-dots i{width:9px;height:9px;border-radius:50%;border:1px solid #888;display:block}
.ring-dots i.on{background:var(--orange);border-color:var(--orange)}
.orange-band{left:0;top:2314px;width:470px;height:3px;background:var(--orange)}

/* footer */
.footer{left:0;top:2653px;width:470px;height:542px;background:linear-gradient(180deg,var(--night) 0%,#1f2b37 55%,var(--night-deep) 100%)}
.contact-card{left:22px;top:2320px;width:425px;height:447px;background:#fff;z-index:2}
.contact-title{top:58px;font-size:30px;font-weight:700;color:var(--ink)}
.contact-sub{top:98px;font-size:14px;color:#333}
.contact-lead{left:33px;top:138px;font-size:16px;color:#333}
.field{left:33px;width:360px;height:30px;border:1px solid #ccc;font-size:10px;color:#999;padding:8px 14px}
.btn-submit{left:277px;top:394px;width:117px;height:30px;background:var(--orange);color:#fff;font-size:13px;font-weight:600;display:flex;align-items:center;justify-content:center}
.foot-brand{top:158px;left:0;width:470px;display:flex;justify-content:center;align-items:center;gap:7px;color:#fff;font-weight:700;font-size:18px}
.foot-brand i{width:12px;height:12px;background:var(--orange);display:block}
.foot-text{top:278px;font-size:12px;line-height:21px;color:#e6e6e6}
.foot-head{top:348px;font-size:13px;font-weight:600;color:#fff;padding-bottom:8px;border-bottom:1px solid #3a4552;width:160px}
.foot-links{font-size:12.5px;color:#fff;line-height:24px}
.subscribe-input{left:261px;top:414px;width:108px;height:25px;background:#fff}
.subscribe-btn{left:369px;top:414px;width:72px;height:25px;background:var(--orange);color:#fff;font-size:10px;display:flex;align-items:center;justify-content:center}
.foot-bottom{left:0;top:472px;width:470px;height:70px;background:#0b1016;border-top:1px solid #26303a}
.copyright{left:32px;top:30px;font-size:10px;color:#ddd}
.social{top:22px;width:24px;height:24px;border:1.5px solid #fff;border-radius:50%}
</style>
</head>
<body>
<main class="screen">

  <header class="site-header abs">
    <div class="menu-toggle abs"><span></span><span></span><span></span></div>
    <div class="brand abs"><i></i>Bright Creek Junk Out</div>
    <div class="btn-estimate abs">Free Estimate</div>
  </header>

  <section class="hero abs">
    <h1 class="hero-title abs center">Best Rated <b>JUNK REMOVEL</b></h1>
    <p class="hero-sub abs center">&amp; Property Cleanout Company in the treasure valley</p>
    <div class="btn-call abs">
      <svg width="11" height="11" viewBox="0 0 24 24"><path fill="#fff" d="M6.6 10.8a15.1 15.1 0 0 0 6.6 6.6l2.2-2.2c.3-.3.7-.4 1-.2 1.1.4 2.3.6 3.6.6.6 0 1 .4 1 1V20c0 .6-.4 1-1 1A17 17 0 0 1 3 4c0-.6.4-1 1-1h3.5c.6 0 1 .4 1 1 0 1.3.2 2.5.6 3.6.1.3 0 .7-.2 1z"/></svg>
      CALL US NOW (555) 010 0147
    </div>
    <div class="hero-photo abs" role="img" aria-label="Company trucks parked in a row under a blue sky"></div>
  </section>

  <div class="rule abs" style="left:220px;top:541px"></div>
  <h2 class="h2 intro-title abs center">Junk Removal and Hauling</h2>
  <p class="intro-text abs center">The Best Rated Junk Hauling and Cleanout<br>Service in the Boise Metro area.</p>

  <div class="intro-circle abs"></div>
  <svg class="hex-photo abs" width="216" height="230" viewBox="0 0 216 230" role="img" aria-label="Team member standing beside a company dump truck">
    <defs><linearGradient id="g1" x1="0" y1="0" x2="0" y2="1"><stop offset="0" stop-color="#8fa7d6"/><stop offset=".55" stop-color="#5a5f66"/><stop offset="1" stop-color="#3a3c40"/></linearGradient></defs>
    <polygon points="108,3 212,60 212,170 108,227 4,170 4,60" fill="url(#g1)" stroke="#111" stroke-width="4"/>
  </svg>
  <div class="badge abs">10+ <small>Years<br>Experience</small></div>

  <p class="intro-body abs">Fastest Response time with Same Day &amp; Next Day service available. We're the Friendliest and Most Professional junk haulers serving Boise, Meridian, Eagle, Star, Middleton, Caldwell, Nampa, Kuna and all of the Treasure Valley.&nbsp; Call us Today ! 555-010-0147</p>
  <div class="btn-outline abs">Book Service Now</div>

  <section class="services abs">
    <h2 class="h2 services-title abs center">Our Services</h2>
    <p class="services-sub abs center">Lorem Ipsum is simply dummy text of the printing.</p>
    <div class="rule abs" style="left:220px;top:212px"></div>

    <svg class="abs" style="left:78px;top:250px" width="320" height="290" viewBox="0 0 320 290" role="img" aria-label="Pile of household junk, tires and wood debris">
      <defs><linearGradient id="g2" x1="0" y1="0" x2="0" y2="1"><stop offset="0" stop-color="#6f8a4a"/><stop offset=".45" stop-color="#8a7560"/><stop offset="1" stop-color="#4b4640"/></linearGradient></defs>
      <polyline points="30,95 4,110 4,240 90,288" fill="none" stroke="#ff9900" stroke-width="2.5"/>
      <polygon points="155,3 284,70 284,205 155,272 26,205 26,70" fill="url(#g2)" stroke="#111" stroke-width="4"/>
      <polygon points="300,36 313,43 313,57 300,64 287,57 287,43" fill="none" stroke="#ff9900" stroke-width="2"/>
    </svg>
    <svg class="abs" style="left:402px;top:248px" width="18" height="20" viewBox="0 0 18 20"><polygon points="9,1 17,5.5 17,14.5 9,19 1,14.5 1,5.5" fill="#dcdce4"/></svg>

    <div class="slide-arrow prev abs"><svg width="12" height="20" viewBox="0 0 12 20"><path d="M10 2 2 10l8 8" fill="none" stroke="#fff" stroke-width="3"/></svg></div>
    <div class="slide-arrow next abs"><svg width="12" height="20" viewBox="0 0 12 20"><path d="M2 2l8 8-8 8" fill="none" stroke="#fff" stroke-width="3"/></svg></div>

    <h3 class="h2 service-name abs center" style="left:-10px">Junk Removal</h3>
    <div class="dotted abs"></div>
    <div class="service-list abs">
      <ul style="left:64px"><li>Misc. Household Junk</li><li>Furniture Removal</li><li>Matterss Removal</li><li>Matterss Removal</li></ul>
      <ul style="left:276px"><li>Hot Tub Removal</li><li>Yard Debris Removal</li><li>Remodeling Debris</li><li>Construction Debris</li></ul>
    </div>
    <svg class="abs" style="left:197px;top:778px" width="76" height="16" viewBox="0 0 76 16"><path d="M2 10c12-8 22 4 36 2S62 2 74 4" fill="none" stroke="#ff9900" stroke-width="3.5" stroke-linecap="round"/></svg>
    <div class="dots abs center" style="top:821px"><i></i><i class="on"></i><i></i></div>
  </section>

  <div class="quote-card abs">
    <div class="quote-mark abs">&ldquo;</div>
    <p class="quote-text abs">Lorem ipsum dolor sit amet, consectetur adipiscing elit. Nullam ac tellus urna. Phasellus dictum et purus iaculis accumsan. Sed suscipit pharetra dolor in venenatis. Vivamus eget finibus ipsum, quis placerat sem. Nulla varius erat in libero ornare dignissim. Nam a interdum.</p>
  </div>
  <div class="avatar abs" role="img" aria-label="Portrait of the co-founder"></div>
  <div class="author abs">DANA WHITFIELD, CO-FOUNDER<small>Northpine</small></div>
  <div class="ring-dots abs center"><i class="on"></i><i></i><i></i></div>
  <div class="orange-band abs"></div>

  <footer class="footer abs" role="img" aria-label="Dark mountain landscape at dusk">
    <div class="foot-brand abs"><i></i>Bright Creek Junk Out</div>
    <p class="foot-text abs center">Lorem ipsum dolor sit amet, consectetur adipiscing<br>elit. Aenean massa mauris, maximus nec faucibus.</p>
    <div class="foot-head abs" style="left:32px">SITELINKS</div>
    <div class="foot-links abs" style="left:32px;top:381px">Home &nbsp;&nbsp;| &nbsp;&nbsp;Our Services<br>What We Take &nbsp;&nbsp;| &nbsp;&nbsp;Contact</div>
    <div class="foot-head abs" style="left:261px;width:180px">STAY IN TOUCH</div>
    <div class="foot-links abs" style="left:261px;top:384px;font-size:11px">Subscribe Our Newsletter</div>
    <div class="subscribe-input abs"></div>
    <div class="subscribe-btn abs">Subscribe</div>
    <div class="foot-bottom abs">
      <div class="copyright abs">@ 2o21 Bright Creek Junk Out. All Rights Reserved.</div>
      <div class="social abs" style="left:357px"></div>
      <div class="social abs" style="left:387px"></div>
      <div class="social abs" style="left:416px"></div>
    </div>
  </footer>

  <section class="contact-card abs">
    <h2 class="contact-title abs center">CONTACT</h2>
    <p class="contact-sub abs center">Lorem ipsum dolor sit amet, consectetur adipiscing.</p>
    <p class="contact-lead abs">Feel Free to Contact Us</p>
    <div class="field abs" style="top:167px">Name</div>
    <div class="field abs" style="top:210px">Email</div>
    <div class="field abs" style="top:253px">Subject</div>
    <div class="field abs" style="top:296px;height:92px">Message...</div>
    <div class="btn-submit abs">SUBMIT</div>
  </section>

</main>
</body>
</html>
```